poster for escape room advertising the themes of our rooms, bold, samples attached

we need poster advertising our 4 escape room themes. The Crimson Ledger, (doctor, test tube) Midnight Carnival, (retro items, time machine) The Velvet Parlour (serial killer, clown, doll, knives) and , moonspire (island, ship, compass). Primarily black and white with red and yellow.
samples attached. Comic book or bold graphic theme. More information can be found on our website quillgatepuzzles.com.

• impact, anything bold, almost comic book

fbee3c
ec1f27
ffffff
000000
5c5c5c
9d9d9d
cbcbcb
e8e8e8
cfcfcf

• title of each room, The Crimson Ledger, Midnight Carnival, The Velvet Parlour, Moonspire. Graphic representing each theme.
• short description of rooms

```html
<!DOCTYPE html>
<html lang="en">
<head>
<meta charset="utf-8">
<title>Quillgate Puzzles – Escape Room Themes</title>
<link rel="stylesheet" href="https://fonts.googleapis.com/css2?family=League+Gothic&family=Pathway+Gothic+One&display=swap">
<style>
  :root {
    --yellow: #fbee3c;
    --yellow-deep: #e8d92f;
    --red: #ec1f27;
    --black: #000000;
    --white: #ffffff;
  }
  * { margin: 0; padding: 0; box-sizing: border-box; }
  html, body { width: 800px; height: 1200px; overflow: hidden; }
  body { background: var(--yellow); font-family: "Pathway Gothic One", "Arial Narrow", sans-serif; }

  .poster {
    position: relative;
    width: 800px;
    height: 1200px;
    background: var(--yellow);
  }

  .room-card {
    position: absolute;
    width: 349px;
    height: 549px;
    background: var(--black);
    overflow: hidden;
  }
  .room-card--ledger    { left: 34px;  top: 34px; }
  .room-card--carnival  { left: 418px; top: 34px; }
  .room-card--parlour   { left: 34px;  top: 618px; }
  .room-card--moonspire { left: 418px; top: 618px; }

  .theme-art {
    position: absolute;
    display: block;
    background: linear-gradient(160deg, var(--yellow) 0%, var(--yellow-deep) 100%);
    border-radius: 6px;
  }
  .theme-icon {
    position: absolute;
    display: block;
    background: var(--red);
    border-radius: 4px;
  }

  .room-title {
    position: absolute;
    left: 0;
    top: 0;
    width: 349px;
    height: 549px;
    pointer-events: none;
  }
  .room-title text {
    font-family: "League Gothic", "Oswald", sans-serif;
    fill: var(--red);
  }

  .room-description {
    position: absolute;
    left: 33px;
    width: 290px;
    top: 476px;
    color: var(--white);
    font-size: 11.5px;
    line-height: 1.34;
  }

  /* The Crimson Ledger */
  .room-card--ledger .theme-art  { left: 36px; top: 34px; width: 284px; height: 220px; }
  .room-card--ledger .theme-icon { left: 78px; top: 292px; width: 52px; height: 70px; border-radius: 4px 4px 18px 18px; }

  /* Midnight Carnival */
  .room-card--carnival .theme-art  { left: 96px; top: 40px; width: 180px; height: 240px; transform: rotate(-14deg); }
  .room-card--carnival .theme-icon { left: 40px; top: 302px; width: 140px; height: 62px; border-radius: 31px; }

  /* The Velvet Parlour */
  .room-card--parlour .theme-art  { left: 0; top: 0; width: 349px; height: 268px; border-radius: 0 0 6px 0; }
  .room-card--parlour .theme-icon { left: 30px; top: 410px; width: 112px; height: 22px; border-radius: 11px 4px 4px 11px; transform: rotate(36deg); }

  /* Moonspire */
  .room-card--moonspire .theme-art  { left: 58px; top: 34px; width: 250px; height: 240px; border-radius: 60px 60px 40px 40px; }
  .room-card--moonspire .theme-icon { left: 148px; top: 310px; width: 56px; height: 56px; border-radius: 50%; }
</style>
</head>
<body>
<main class="poster">

  <article class="room-card room-card--ledger">
    <span class="theme-art" role="img" aria-label="Yellow and white illustration of a test tube rack, stethoscope, syringe, pen and a spilled puddle"></span>
    <span class="theme-icon" role="img" aria-label="Red laboratory flask icon"></span>
    <svg class="room-title" viewBox="0 0 349 549" role="heading" aria-level="2" aria-label="The Crimson Ledger">
      <text x="138" y="358" font-size="92" textLength="68" lengthAdjust="spacingAndGlyphs">The</text>
      <text x="50" y="438" font-size="92" textLength="252" lengthAdjust="spacingAndGlyphs">Crimson Ledger</text>
    </svg>
    <p class="room-description">Millions of people across the world have been infected with a life-threatening virus. You and your team have been tasked with the investigation. What you learn will put you and your friends at risk, as you shed light on a larger conspiracy.</p>
  </article>

  <article class="room-card room-card--carnival">
    <span class="theme-art" role="img" aria-label="Yellow illustration of a retro handheld game console showing a game over screen"></span>
    <span class="theme-icon" role="img" aria-label="Red row of three gears, one with a rewind arrow"></span>
    <svg class="room-title" viewBox="0 0 349 549" role="heading" aria-level="2" aria-label="Midnight Carnival">
      <text x="34" y="438" font-size="92" textLength="282" lengthAdjust="spacingAndGlyphs">Midnight Carnival</text>
    </svg>
    <p class="room-description">Jessica loves the 90's. You could say she's stuck there, and she wants your company. You have 1 hour to escape her apartment, otherwise, the time machine she has been working on will be activated and you'll spend an eternity stuck in the 90's.</p>
  </article>

  <article class="room-card room-card--parlour">
    <span class="theme-art" role="img" aria-label="Yellow crossed chains with a white padlock, a white spider web and a reaching yellow arm"></span>
    <span class="theme-icon" role="img" aria-label="Red knife icon"></span>
    <svg class="room-title" viewBox="0 0 349 549" role="heading" aria-level="2" aria-label="The Velvet Parlour">
      <text x="34" y="364" font-size="96" textLength="282" lengthAdjust="spacingAndGlyphs">The Velvet</text>
      <text x="316" y="442" font-size="96" text-anchor="end" textLength="166" lengthAdjust="spacingAndGlyphs">Parlour</text>
    </svg>
    <p class="room-description">On a quest to save your friend, you find yourself trapped in the lair of a murderous psychopath. You must find out where your friend is and how to save them. Will you be able to stop this maniac, or will you soon need a friend to save you?</p>
  </article>

  <article class="room-card room-card--moonspire">
    <span class="theme-art" role="img" aria-label="Yellow silhouette of a small island with palm trees and two white seagulls"></span>
    <span class="theme-icon" role="img" aria-label="Red compass rose"></span>
    <svg class="room-title" viewBox="0 0 349 549" role="heading" aria-level="2" aria-label="Moonspire">
      <text x="34" y="438" font-size="96" textLength="280" lengthAdjust="spacingAndGlyphs">Moonspire</text>
    </svg>
    <p class="room-description">On a quest to save your friend, you find yourself trapped in the lair of a murderous psychopath. You must find out where your friend is and how to save them. Will you be able to stop this maniac, or will you soon need a friend to save you?</p>
  </article>

</main>
</body>
</html>
```